(Wix) Website Design Tweaks

The site: www.LanternAndLoomly.com
(The coding must be done within Wix. I will create a duplicate website so you can gain access and begin editing.)

My website contains my preferred text and images - but it needs to look more professional. My business focuses on "Corporate Messaging" and "Marketing Communications", so the website needs to look professional, but not too corporate. My clients range from very big companies to technology startups - the look and feel should be uncluttered, professional, and modern.

I want someone to review the pages, and make changes / suggestions focused on:
1) Fonts
2) Colors
3) Layout

If you have ideas for adding additional graphics, that's fine, but they should be consistent with what I already have . . . unless you think some / all of my images need to be changed.

My site is very, very small, and only contains 5 (very short) pages. There are no sub-pages. (One page is the contact page, with almost nothing except form fields.)

If you do a good job with my site, I may be able to provide you with additional work - many of my clients need website design tweaks, after I provide the verbiage.

```html
<!DOCTYPE html>
<html lang="en">
<head>
<meta charset="utf-8">
<title>Lantern &amp; Loomly — Corporate Messaging and Marketing Communications</title>
<link rel="stylesheet" href="https://fonts.googleapis.com/css2?family=Montserrat:ital,wght@0,400;0,500;0,600;1,400&family=Raleway:wght@300;400&display=swap">
<style>
:root{
  --navy:#0f2a4a;
  --navy-deep:#13253d;
  --footer:#1c2633;
  --accent:#c8772a;
  --ink:#1b1b1b;
  --muted:#555a60;
  --rule:#cfd3d8;
  --band:#f3f3f3;
  --white:#ffffff;
}
*{box-sizing:border-box;margin:0;padding:0}
html,body{width:1200px;height:3868px;overflow:hidden}
body{position:relative;background:var(--white);font-family:"Raleway",sans-serif;color:var(--ink)}
.abs{position:absolute}
.heading{font-family:"Montserrat",sans-serif;font-weight:500;text-align:center;letter-spacing:.5px}

/* header */
.site-header{left:0;top:0;width:1200px;height:80px;background:var(--navy)}
.brand{left:142px;top:13px;color:var(--white);font-family:"Montserrat",sans-serif;font-weight:400;font-size:25px;line-height:26px;letter-spacing:1px}
.nav{top:30px;left:0;font-family:"Montserrat",sans-serif;font-weight:500;font-size:13.5px;color:var(--white)}
.nav span{position:absolute;white-space:nowrap}
.nav .active{border-bottom:2px solid var(--white);padding-bottom:5px}
.user-icon{left:1036px;top:28px}

/* hero */
.hero{left:0;top:80px;width:1200px;height:588px;background:linear-gradient(120deg,#2c4668 0%,#6f8fb3 35%,#a8c0d8 60%,#4f6f98 100%)}
.hero-card{left:267px;top:511px;width:666px;height:190px;background:var(--white)}
.hero-title{left:267px;top:550px;width:666px;font-size:41px;color:var(--ink);font-weight:500}
.hero-sub{left:267px;top:615px;width:666px;font-family:"Montserrat",sans-serif;font-size:16px;text-align:center;font-weight:500}
.btn-outline{border:2.5px solid var(--accent);background:transparent;font-family:"Montserrat",sans-serif;font-weight:500;font-size:18px;text-align:center;color:var(--navy)}
.hero-btn{left:488px;top:654px;width:224px;height:54px;line-height:49px}

/* services */
.services{left:144px;top:755px;width:912px;height:435px;border:1.5px solid var(--rule)}
.divider{width:1.5px;background:var(--rule)}
.col-title{font-size:23px;color:var(--ink)}
.col-text{font-size:12px;line-height:22px;color:var(--muted);text-align:center}
.col-text.justify{text-align:justify;text-align-last:center}
.btn-solid{background:var(--navy);color:var(--white);font-family:"Montserrat",sans-serif;font-weight:500;font-size:13.5px;text-align:center;width:136px;height:43px;line-height:43px}

/* challenge */
.challenge{left:0;top:1257px;width:1200px;height:538px;background:linear-gradient(110deg,#e6eef7 0%,#dbe7f3 40%,#c9dbee 70%,#e0eaf5 100%)}
.challenge-title{left:0;top:1350px;width:1200px;font-size:40px;color:var(--navy)}
.challenge-text{left:250px;top:1444px;width:700px;font-size:15.5px;line-height:28px;color:#3c4148;text-align:justify;text-align-last:center}
.challenge-btn{left:488px;top:1630px;width:224px;height:54px;line-height:49px}

/* clients */
.clients-title{left:0;top:1884px;width:1200px;font-size:40px;color:var(--navy)}
.clients{left:144px;top:1990px;width:912px;height:206px;border:1.5px solid var(--rule)}
.client{font-family:"Montserrat",sans-serif;font-weight:500;font-size:16px;color:var(--navy);text-align:center;line-height:22px}
.client .mark{display:inline-block;width:12px;height:12px;background:var(--navy);margin-right:8px;vertical-align:-1px}

/* testimonials */
.testimonials{left:0;top:2294px;width:1200px;height:473px;background:var(--band)}
.testimonials-title{left:0;top:2378px;width:1200px;font-size:40px;color:var(--navy)}
.quote{left:220px;top:2484px;width:760px;font-family:"Montserrat",sans-serif;font-style:italic;font-size:16.5px;line-height:28px;color:#3c4148;text-align:center}
.attribution{left:0;top:2590px;width:1200px;font-family:"Montserrat",sans-serif;font-weight:600;font-size:16px;text-align:center;color:var(--ink)}
.dot{width:8px;height:8px;border-radius:50%;background:var(--ink)}
.dot.current{width:11px;height:11px;background:transparent;border:1.5px solid var(--ink)}

/* contact */
.contact{left:0;top:2767px;width:1200px;height:1021px;background:var(--navy)}
.contact-title{left:0;top:2862px;width:1200px;font-size:40px;color:var(--white)}
.field-label{font-family:"Montserrat",sans-serif;font-size:13px;color:var(--white)}
.field-line{height:2px;background:var(--white)}
.submit{left:488px;top:3312px;width:224px;height:54px;line-height:49px;color:var(--white)}
.map{left:144px;top:3421px;width:912px;height:311px;background:linear-gradient(135deg,#b9b9b9 0%,#a6a6a6 50%,#bcbcbc 100%)}
.chat{left:1113px;top:3755px;width:53px;height:53px;background:var(--navy);border:1.5px solid #3b5575}

/* footer */
.site-footer{left:0;top:3788px;width:1200px;height:80px;background:var(--footer)}
.footer-text{left:143px;top:3822px;font-family:"Montserrat",sans-serif;font-size:11.5px;color:var(--white)}
.social{width:11px;height:11px;border-radius:50%;background:var(--white)}
</style>
</head>
<body>

<header class="abs site-header">
  <div class="abs brand">LANTERN &amp;<br>LOOMLY</div>
  <nav class="abs nav">
    <span class="active" style="left:470px">HOME</span>
    <span style="left:550px">LANTERNCAMP</span>
    <span style="left:697px">TESTIMONIALS</span>
    <span style="left:843px">TEAM</span>
    <span style="left:917px">CONTACT</span>
  </nav>
  <svg class="abs user-icon" width="22" height="24" viewBox="0 0 22 24" fill="none" stroke="#fff" stroke-width="2">
    <circle cx="11" cy="7" r="5"/><path d="M2 22c0-5 4-8 9-8s9 3 9 8z"/>
  </svg>
</header>

<section class="abs hero" role="img" aria-label="Photo of a person typing on a laptop overlaid with glowing data charts and network lines"></section>
<div class="abs hero-card"></div>
<h1 class="abs heading hero-title">INFORM. INFLUENCE.SELL.</h1>
<p class="abs hero-sub">Corporate Messaging and Marketing Communications</p>
<div class="abs btn-outline hero-btn">GET STARTED</div>

<section class="abs services"></section>
<div class="abs divider" style="left:448px;top:799px;height:346px"></div>
<div class="abs divider" style="left:763px;top:799px;height:346px"></div>

<h2 class="abs heading col-title" style="left:175px;top:824px;width:220px">HOW WE HELP</h2>
<p class="abs col-text justify" style="left:175px;top:876px;width:220px">At Lantern &amp; Loomly, we help individuals and organizations “get what they want” through clear and persuasive communication. Our consulting, coaching, and training services help clients achieve targeted business objectives, with an emphasis on informing, influencing, and selling.</p>
<div class="abs btn-solid" style="left:217px;top:1069px">MORE INFO</div>

<h2 class="abs heading col-title" style="left:470px;top:824px;width:260px">EXPERTISE</h2>
<p class="abs col-text" style="left:470px;top:876px;width:260px">Sales Training<br>Presentation Skills Training<br>Stage Talks<br>Elevator Pitches<br>Keynote Speeches<br>Marketing Collateral<br>Business Presentations &amp; Decks<br>Venture Capital Presentations &amp; Decks</p>
<div class="abs btn-solid" style="left:532px;top:1069px">MORE INFO</div>

<h2 class="abs heading col-title" style="left:793px;top:824px;width:240px">RESULTS</h2>
<p class="abs col-text" style="left:800px;top:876px;width:226px">Whatever the message, and whatever the medium, we help clients establish a connection, make an impression, and drive audiences toward a predetermined course of action. This results in clear messaging, captivated audiences, and increased sales.</p>
<div class="abs btn-solid" style="left:846px;top:1069px">MORE INFO</div>

<section class="abs challenge" role="img" aria-label="Faded photo of business people working at a desk with laptops and paperwork"></section>
<h2 class="abs heading challenge-title">THE BIG CHALLENGE</h2>
<p class="abs challenge-text">In today’s competitive business environment, effective communication is more essential than ever before. It is the foundation upon which companies are built, careers are propelled, and knowledge is imparted. Effective communication is critical - without it, misunderstandings arise, errors occur, and business goals are frustrated. In short, effective communication is the key driver of long-term business and professional success.</p>
<div class="abs btn-outline challenge-btn">READ MORE</div>

<h2 class="abs heading clients-title">OUR CLIENTS</h2>
<section class="abs clients"></section>
<div class="abs divider" style="left:367px;top:1992px;height:202px"></div>
<div class="abs divider" style="left:606px;top:1992px;height:202px"></div>
<div class="abs divider" style="left:815px;top:1992px;height:202px"></div>
<div class="abs client" style="left:150px;top:2071px;width:217px"><span class="mark"></span>Harbor City<br>Guild</div>
<div class="abs client" style="left:369px;top:2071px;width:237px">Meridian Care<br>Partners</div>
<div class="abs client" style="left:608px;top:2071px;width:207px">Westbrook<br>Business School</div>
<div class="abs client" style="left:817px;top:2071px;width:237px"><span class="mark"></span>Granite Row<br>Holdings</div>

<section class="abs testimonials"></section>
<h2 class="abs heading testimonials-title">TESTIMONIALS</h2>
<p class="abs quote">Good morning Evan - Thank you for all the time and effort you dedicated to helping me get this speech ready. It’s a big one, and there is no way I could have pulled it off without your gentle guidance and tough love. Let’s hope the cameras get my good side!</p>
<p class="abs attribution">- DANIEL R. &nbsp;|&nbsp; ECONOMIST &amp; AWARD-WINNING AUTHOR</p>
<div class="abs dot current" style="left:572px;top:2669px"></div>
<div class="abs dot" style="left:597px;top:2670px"></div>
<div class="abs dot" style="left:620px;top:2670px"></div>

<section class="abs contact"></section>
<h2 class="abs heading contact-title">CONTACT</h2>
<label class="abs field-label" style="left:200px;top:2976px">First Name</label>
<div class="abs field-line" style="left:200px;top:3016px;width:377px"></div>
<label class="abs field-label" style="left:622px;top:2976px">Last Name</label>
<div class="abs field-line" style="left:622px;top:3016px;width:377px"></div>
<label class="abs field-label" style="left:200px;top:3073px">Email *</label>
<div class="abs field-line" style="left:200px;top:3113px;width:377px"></div>
<label class="abs field-label" style="left:622px;top:3073px">Subject*</label>
<div class="abs field-line" style="left:622px;top:3113px;width:377px"></div>
<label class="abs field-label" style="left:200px;top:3161px">Message*</label>
<div class="abs field-line" style="left:200px;top:3257px;width:799px"></div>
<div class="abs btn-outline submit">SUBMIT</div>

<div class="abs map" role="img" aria-label="Road map of the eastern United States marking the office location"></div>

<div class="abs chat">
  <svg width="50" height="50" viewBox="0 0 50 50">
    <circle cx="25" cy="24" r="11" fill="#fff"/><path d="M17 31l-3 6 8-3z" fill="#fff"/>
    <circle cx="21" cy="24" r="1.6" fill="#13253d"/><circle cx="25" cy="24" r="1.6" fill="#13253d"/><circle cx="29" cy="24" r="1.6" fill="#13253d"/>
  </svg>
</div>

<footer class="abs site-footer"></footer>
<p class="abs footer-text">2022 Lantern &amp; Loomly Communications.Al Rights Reserved &nbsp;| Privacy Policy &nbsp;| &nbsp;Terms and Use</p>
<div class="abs social" style="left:1017px;top:3826px"></div>
<div class="abs social" style="left:1041px;top:3826px"></div>

</body>
</html>
```